Brennick Holdings Business Cards

These are professional business cards that are for my family office.
Put fake emails and phone numbers as of now until I finalize those components. This family office controls my families investments, assets, and future. The cards should be professional.
..
.
.
.
I just uploaded another variation of a logo I would like to see as a business card to I am inbeteen which logo to use

Target Market(s)

business

Industry/Entity Type

business

Contact Information for Business Card

Professional, wealth related, finance related.

Requirements
Must have
• Logo

```html
<!DOCTYPE html>
<html lang="en">
<head>
<meta charset="utf-8">
<title>Brennick Holdings Business Cards</title>
<link rel="stylesheet" href="https://fonts.googleapis.com/css2?family=Libre+Baskerville:ital,wght@0,400;0,700;1,400&display=swap">
<style>
  :root {
    --backdrop: #0d0e12;
    --card: #141925;
    --card-edge: #1b2131;
    --emboss: #232a3b;
    --emboss-light: #2c3447;
    --silver: #a3a5ad;
    --ink-light: #eceef2;
    --icon: #8d9099;
    --faint: #1d2333;
  }
  * { box-sizing: border-box; margin: 0; padding: 0; }
  html, body {
    width: 1200px; height: 963px; overflow: hidden;
    background: var(--backdrop);
    font-family: "Libre Baskerville", "Palatino Linotype", serif;
  }
  .sheet {
    position: relative; width: 1200px; height: 963px;
    display: flex; align-items: center; justify-content: center; gap: 48px;
  }
  .card {
    position: relative; width: 520px; height: 297px;
    background: var(--card);
    border: 1px solid var(--card-edge);
    box-shadow: 0 18px 40px rgba(0,0,0,.55);
    overflow: hidden;
  }
  /* Front */
  .card--front { display: flex; align-items: center; justify-content: center; gap: 18px; }
  .brand-dot {
    width: 46px; height: 46px; border-radius: 50%;
    border: 2px solid var(--emboss-light);
  }
  .brand-name {
    font-size: 25px; letter-spacing: 3px; text-transform: uppercase;
    color: var(--emboss-light);
  }
  /* Back */
  .backdrop-circle {
    position: absolute; left: 150px; top: 30px;
    width: 238px; height: 238px; border-radius: 50%;
    border: 3px solid var(--faint);
  }
  .identity {
    position: absolute; right: 268px; top: 92px; text-align: right;
  }
  .identity__name {
    font-size: 17px; letter-spacing: 1px; text-transform: uppercase;
    color: var(--silver); white-space: nowrap;
  }
  .identity__role { font-size: 12.5px; color: var(--ink-light); margin-top: 4px; }
  .divider {
    position: absolute; left: 262px; top: 96px; width: 1px; height: 68px;
    background: #3a4152;
  }
  .contacts {
    position: absolute; left: 276px; top: 104px; list-style: none;
    font-size: 12.5px; color: var(--ink-light);
  }
  .contacts li { display: flex; align-items: center; gap: 8px; height: 20px; }
  .contacts svg { width: 13px; height: 13px; flex: none; }
  .address {
    position: absolute; left: 0; right: 0; top: 196px; text-align: center;
    font-size: 12.5px; color: var(--ink-light);
  }
</style>
</head>
<body>
<main class="sheet">
  <section class="card card--front" aria-label="Card front">
    <span class="brand-dot"></span>
    <span class="brand-name">Brennick Holdings</span>
  </section>

  <section class="card card--back" aria-label="Card back">
    <span class="backdrop-circle"></span>
    <div class="identity">
      <p class="identity__name">Daniel Harrow</p>
      <p class="identity__role">Manager</p>
    </div>
    <span class="divider"></span>
    <ul class="contacts">
      <li>
        <svg viewBox="0 0 16 16" aria-hidden="true"><path fill="var(--icon)" d="M3 2h3l1 3-2 1a9 9 0 0 0 5 5l1-2 3 1v3a1 1 0 0 1-1 1A12 12 0 0 1 2 3a1 1 0 0 1 1-1z"/></svg>
        123-456-2100
      </li>
      <li>
        <svg viewBox="0 0 16 16" aria-hidden="true"><rect x="1.5" y="3.5" width="13" height="9" fill="none" stroke="var(--icon)" stroke-width="1.5"/><path d="M1.5 3.5 8 9l6.5-5.5" fill="none" stroke="var(--icon)" stroke-width="1.5"/></svg>
        youremail@brennickmail.com
      </li>
      <li>
        <svg viewBox="0 0 16 16" aria-hidden="true"><circle cx="8" cy="8" r="6.5" fill="none" stroke="var(--icon)" stroke-width="1.5"/><path d="M1.5 8h13M8 1.5c-3 3.5-3 9.5 0 13M8 1.5c3 3.5 3 9.5 0 13" fill="none" stroke="var(--icon)" stroke-width="1.2"/></svg>
        www.yourwebsite.com
      </li>
    </ul>
    <p class="address">Your Address, City, State, Zip 0000</p>
  </section>
</main>
</body>
</html>
```